Torvane PowerPoint Template

I have a company called Torvane, LLC and my company logo is already designed. I need a PowerPoint template that I will be using to pitch potential investors and business partners. This should be a very professional-looking template that leverages the company logo colors and really pops. The company is an AI product research and development company.

```html
<!DOCTYPE html>
<html lang="en">
<head>
<meta charset="utf-8">
<title>Torvane Presentation Template</title>
<link href="https://fonts.googleapis.com/css2?family=Inter+Tight:wght@500;600;700;800&family=Inter:wght@400;500;600;700&display=swap" rel="stylesheet">
<style>
  :root{
    --canvas:#7b7b7b;
    --paper:#ffffff;
    --red:#c8232c;
    --ink:#3b3b3b;
    --black:#111111;
    --muted:#666666;
    --track:#e4e4e4;
    --line:#bdbdbd;
  }
  html,body{margin:0;padding:0;width:986px;height:1200px;overflow:hidden;background:var(--canvas);}
  .board{position:relative;width:986px;height:1200px;}
  .slide{position:absolute;width:431px;height:243px;background:var(--paper);display:block;}
  .s-cover{left:45px;top:61px}
  .s-chart{left:510px;top:61px}
  .s-agenda{left:45px;top:340px}
  .s-donuts{left:510px;top:340px}
  .s-about{left:45px;top:618px}
  .s-process{left:510px;top:618px}
  .s-services{left:45px;top:897px}
  .s-contact{left:510px;top:897px}
  .head{font-family:"Inter Tight",sans-serif;font-weight:700;letter-spacing:-1px;}
  .brand{font-family:"Inter Tight",sans-serif;font-weight:700;fill:var(--ink);letter-spacing:-0.8px;}
  .body{font-family:"Inter",sans-serif;}
  .bold{font-family:"Inter",sans-serif;font-weight:600;}
  .red{fill:var(--red)}
  .ink{fill:var(--ink)}
  .muted{fill:var(--muted)}
  .white{fill:#fff}
</style>
</head>
<body>
<div class="board">

<!-- Cover -->
<svg class="slide s-cover" viewBox="0 0 758 427" xmlns="http://www.w3.org/2000/svg">
  <defs>
    <linearGradient id="coverPhoto" x1="0" y1="0" x2="1" y2="1">
      <stop offset="0" stop-color="#e9d9d6"/>
      <stop offset="0.5" stop-color="#c9b7ae"/>
      <stop offset="1" stop-color="#2e3a52"/>
    </linearGradient>
  </defs>
  <circle cx="48" cy="45" r="20" class="red"/>
  <text x="78" y="58" class="brand" font-size="36">Torvane</text>
  <text x="26" y="195" class="head red" font-size="44">Presentation</text>
  <text x="26" y="250" class="head ink" font-size="44">Slide Title Here</text>
  <line x1="0" y1="276" x2="345" y2="276" stroke="var(--red)" stroke-width="3"/>
  <circle cx="345" cy="276" r="5" class="red"/>
  <text x="28" y="313" class="body ink" font-size="16" font-weight="500">Your Subtitle Goes Here</text>
  <rect x="27" y="341" width="130" height="34" rx="17" fill="none" stroke="var(--red)" stroke-width="2"/>
  <text x="92" y="362" class="body red" font-size="10" text-anchor="middle" font-weight="500">MONTH XX, 2024</text>
  <g role="img" aria-label="Photo of two smiling business professionals holding tablets">
    <rect x="360" y="40" width="398" height="387" fill="url(#coverPhoto)"/>
  </g>
</svg>

<!-- Bar chart -->
<svg class="slide s-chart" viewBox="0 0 758 427" xmlns="http://www.w3.org/2000/svg">
  <text x="27" y="43" class="head" font-size="30"><tspan class="red">Title</tspan><tspan class="ink"> Goes Here</tspan></text>
  <circle cx="589" cy="33" r="16" class="red"/>
  <text x="613" y="44" class="brand" font-size="30">Torvane</text>
  <g class="body ink" font-size="7" text-anchor="end">
    <text x="66" y="124">6</text><text x="66" y="158">5</text><text x="66" y="192">4</text>
    <text x="66" y="226">3</text><text x="66" y="260">2</text><text x="66" y="294">1</text><text x="66" y="329">0</text>
  </g>
  <g stroke="#e6e6e6" stroke-width="1">
    <line x1="75" y1="121" x2="432" y2="121"/><line x1="75" y1="155" x2="432" y2="155"/>
    <line x1="75" y1="189" x2="432" y2="189"/><line x1="75" y1="223" x2="432" y2="223"/>
    <line x1="75" y1="257" x2="432" y2="257"/><line x1="75" y1="291" x2="432" y2="291"/>
  </g>
  <line x1="75" y1="326" x2="432" y2="326" stroke="#999"/>
  <g>
    <rect x="88" y="180" width="14" height="146" class="red"/><rect x="108" y="244" width="14" height="82" fill="#444"/><rect x="128" y="258" width="14" height="68" fill="var(--black)"/>
    <rect x="178" y="180" width="14" height="146" class="red"/><rect x="198" y="244" width="14" height="82" fill="#444"/><rect x="218" y="258" width="14" height="68" fill="var(--black)"/>
    <rect x="268" y="180" width="14" height="146" class="red"/><rect x="288" y="244" width="14" height="82" fill="#444"/><rect x="308" y="258" width="14" height="68" fill="var(--black)"/>
    <rect x="358" y="180" width="14" height="146" class="red"/><rect x="378" y="244" width="14" height="82" fill="#444"/><rect x="398" y="258" width="14" height="68" fill="var(--black)"/>
  </g>
  <g class="body ink" font-size="7" text-anchor="middle">
    <text x="115" y="338">Category 1</text><text x="205" y="338">Category 1</text>
    <text x="295" y="338">Category 1</text><text x="385" y="338">Category 1</text>
  </g>
  <g class="body muted" font-size="8.5">
    <circle cx="488" cy="98" r="9" class="red"/>
    <text x="510" y="102" class="bold ink" font-size="16">Title Goes Here</text>
    <text x="510" y="123">Lorem ipsum dolor sit amet, consectetur</text>
    <text x="510" y="135">adipiscing elit, sed dolore magna aliqua. Ut</text>
    <text x="510" y="147">enim exercitation ullamco laboris nisi ut</text>
    <text x="510" y="159">aliquip ex ea commodo consequat.</text>
    <circle cx="488" cy="201" r="9" fill="#444"/>
    <text x="510" y="205" class="bold ink" font-size="16">Title Goes Here</text>
    <text x="510" y="226">Lorem ipsum dolor sit amet, consectetur</text>
    <text x="510" y="238">adipiscing elit, sed dolore magna aliqua. Ut</text>
    <text x="510" y="250">enim exercitation ullamco laboris nisi ut</text>
    <text x="510" y="262">aliquip ex ea commodo consequat.</text>
    <circle cx="488" cy="304" r="9" fill="var(--black)"/>
    <text x="510" y="308" class="bold ink" font-size="16">Title Goes Here</text>
    <text x="510" y="329">Lorem ipsum dolor sit amet, consectetur</text>
    <text x="510" y="341">adipiscing elit, sed dolore magna aliqua. Ut</text>
    <text x="510" y="353">enim exercitation ullamco laboris nisi ut</text>
    <text x="510" y="365">aliquip ex ea commodo consequat.</text>
  </g>
  <text x="27" y="411" class="body ink" font-size="8">© 2025, Torvane, LLC. All rights Reserved.</text>
  <line x1="215" y1="408" x2="707" y2="408" stroke="var(--red)" stroke-width="2"/>
  <circle cx="718" cy="408" r="11" fill="#fff" stroke="var(--red)" stroke-width="1.5"/>
  <text x="718" y="411" class="body ink" font-size="8" text-anchor="middle">05</text>
</svg>

<!-- Agenda -->
<svg class="slide s-agenda" viewBox="0 0 758 427" xmlns="http://www.w3.org/2000/svg">
  <defs>
    <linearGradient id="agendaPhoto" x1="0" y1="0" x2="0" y2="1">
      <stop offset="0" stop-color="#b9c8d8"/>
      <stop offset="0.6" stop-color="#7f93a6"/>
      <stop offset="1" stop-color="#3d4650"/>
    </linearGradient>
    <filter id="soft" x="-10%" y="-30%" width="120%" height="160%"><feDropShadow dx="0" dy="1" stdDeviation="2" flood-opacity="0.15"/></filter>
  </defs>
  <g role="img" aria-label="Photo of a businesswoman using a tablet by a window over a city skyline">
    <rect x="0" y="0" width="306" height="427" fill="url(#agendaPhoto)"/>
  </g>
  <text x="368" y="40" class="head" font-size="30"><tspan class="red">Our</tspan><tspan class="ink"> Agenda</tspan></text>
  <circle cx="612" cy="33" r="14" class="red"/>
  <text x="633" y="43" class="brand" font-size="26">Torvane</text>
  <g id="agendaItems" class="bold" font-size="15">
    <g transform="translate(0,97)"><rect x="425" y="-18" width="305" height="36" fill="#fff" filter="url(#soft)"/><rect x="727" y="-18" width="3" height="36" class="red"/><polygon points="385,-16 399,-8 399,8 385,16 371,8 371,-8" class="red"/><text x="385" y="4" class="white" font-size="10" text-anchor="middle">01</text><text x="455" y="6" class="ink">Introduction</text></g>
    <g transform="translate(0,152)"><rect x="425" y="-18" width="305" height="36" fill="#fff" filter="url(#soft)"/><rect x="727" y="-18" width="3" height="36" class="ink"/><polygon points="385,-16 399,-8 399,8 385,16 371,8 371,-8" fill="#444"/><text x="385" y="4" class="white" font-size="10" text-anchor="middle">02</text><text x="455" y="6" class="ink">Our Team</text></g>
    <g transform="translate(0,207)"><rect x="425" y="-18" width="305" height="36" fill="#fff" filter="url(#soft)"/><rect x="727" y="-18" width="3" height="36" class="ink"/><polygon points="385,-16 399,-8 399,8 385,16 371,8 371,-8" fill="#444"/><text x="385" y="4" class="white" font-size="10" text-anchor="middle">03</text><text x="455" y="6" class="ink">Statistics</text></g>
    <g transform="translate(0,263)"><rect x="425" y="-18" width="305" height="36" fill="#fff" filter="url(#soft)"/><rect x="727" y="-18" width="3" height="36" class="ink"/><polygon points="385,-16 399,-8 399,8 385,16 371,8 371,-8" fill="#444"/><text x="385" y="4" class="white" font-size="10" text-anchor="middle">04</text><text x="455" y="6" class="ink">Graph</text></g>
    <g transform="translate(0,318)"><rect x="425" y="-18" width="305" height="36" fill="#fff" filter="url(#soft)"/><rect x="727" y="-18" width="3" height="36" class="ink"/><polygon points="385,-16 399,-8 399,8 385,16 371,8 371,-8" fill="#444"/><text x="385" y="4" class="white" font-size="10" text-anchor="middle">05</text><text x="455" y="6" class="ink">Testimonial</text></g>
    <g transform="translate(0,373)"><rect x="425" y="-18" width="305" height="36" fill="#fff" filter="url(#soft)"/><rect x="727" y="-18" width="3" height="36" class="ink"/><polygon points="385,-16 399,-8 399,8 385,16 371,8 371,-8" fill="#444"/><text x="385" y="4" class="white" font-size="10" text-anchor="middle">06</text><text x="455" y="6" class="ink">Contact Us</text></g>
  </g>
</svg>

<!-- Donut stats -->
<svg class="slide s-donuts" viewBox="0 0 758 427" xmlns="http://www.w3.org/2000/svg">
  <text x="27" y="43" class="head" font-size="30"><tspan class="red">Title</tspan><tspan class="ink"> Goes Here</tspan></text>
  <circle cx="589" cy="33" r="16" class="red"/>
  <text x="613" y="44" class="brand" font-size="30">Torvane</text>
  <g fill="none" stroke-width="14">
    <circle cx="163" cy="178" r="72" stroke="var(--track)"/>
    <circle cx="163" cy="178" r="72" stroke="var(--black)" stroke-dasharray="158.3 452.4" transform="rotate(-90 163 178)"/>
    <circle cx="380" cy="178" r="72" stroke="var(--track)"/>
    <circle cx="380" cy="178" r="72" stroke="var(--red)" stroke-dasharray="294 452.4" transform="rotate(-90 380 178)"/>
    <circle cx="597" cy="178" r="72" stroke="var(--track)"/>
    <circle cx="597" cy="178" r="72" stroke="#444" stroke-dasharray="384.5 452.4" transform="rotate(-90 597 178)"/>
  </g>
  <g class="bold" font-size="23" text-anchor="middle">
    <text x="163" y="186" fill="var(--black)">35%</text>
    <text x="380" y="186" class="red">65%</text>
    <text x="597" y="186" fill="#444">85%</text>
  </g>
  <g class="bold" font-size="15" text-anchor="middle">
    <text x="162" y="292" class="ink">Heading Goes Here</text>
    <text x="379" y="292" class="red">Heading Goes Here</text>
    <text x="596" y="292" class="ink">Heading Goes Here</text>
  </g>
  <g class="body muted" font-size="8.5" text-anchor="middle">
    <text x="162" y="313">Lorem ipsum dolor sit amet, consectetur</text><text x="162" y="326">adipiscing elit, sed do eiusmod tempor</text><text x="162" y="339">incididunt ut labore et dolore magna</text><text x="162" y="352">enim ad minim aliqua.</text>
    <text x="379" y="313">Lorem ipsum dolor sit amet, consectetur</text><text x="379" y="326">adipiscing elit, sed do eiusmod tempor</text><text x="379" y="339">incididunt ut labore et dolore magna</text><text x="379" y="352">enim ad minim aliqua.</text>
    <text x="596" y="313">Lorem ipsum dolor sit amet, consectetur</text><text x="596" y="326">adipiscing elit, sed do eiusmod tempor</text><text x="596" y="339">incididunt ut labore et dolore magna</text><text x="596" y="352">enim ad minim aliqua.</text>
  </g>
  <text x="27" y="411" class="body ink" font-size="8">© 2025, Torvane, LLC. All rights Reserved.</text>
  <line x1="215" y1="408" x2="707" y2="408" stroke="var(--red)" stroke-width="2"/>
  <circle cx="718" cy="408" r="11" fill="#fff" stroke="var(--red)" stroke-width="1.5"/>
  <text x="718" y="411" class="body ink" font-size="8" text-anchor="middle">06</text>
</svg>

<!-- Who we are -->
<svg class="slide s-about" viewBox="0 0 758 427" xmlns="http://www.w3.org/2000/svg">
  <defs>
    <linearGradient id="aboutPhoto" x1="0" y1="0" x2="1" y2="1">
      <stop offset="0" stop-color="#cfc9bf"/>
      <stop offset="0.55" stop-color="#9a8a78"/>
      <stop offset="1" stop-color="#5a4636"/>
    </linearGradient>
  </defs>
  <text x="27" y="45" class="head" font-size="30"><tspan class="red">Who</tspan><tspan class="ink"> We Are</tspan></text>
  <circle cx="589" cy="33" r="16" class="red"/>
  <text x="613" y="44" class="brand" font-size="30">Torvane</text>
  <circle cx="180" cy="226" r="152" fill="none" stroke="var(--red)" stroke-width="2"/>
  <circle cx="180" cy="226" r="146" fill="none" stroke="var(--red)" stroke-width="1"/>
  <g role="img" aria-label="Photo of colleagues shaking hands across a meeting table">
    <circle cx="180" cy="226" r="137" fill="url(#aboutPhoto)"/>
  </g>
  <g class="body muted" font-size="10">
    <text x="383" y="109">Lorem ipsum dolor sit amet, consectetur adipiscing elit, sed do eius-</text>
    <text x="383" y="127">mod tempor incididunt ut labore et dolore magna aliqua. Ut enim ad</text>
    <text x="383" y="146">minim veniam, quis nostrud exercitation ullamco laboris nisi ut aliquip</text>
    <text x="383" y="164">ex ea commodo consequat. Duis aute irure dolor in reprehenderit in vo-</text>
    <text x="383" y="183">luptate velit esse cillum dolore eu fugiat nulla pariatur. Excepteur sint</text>
    <text x="383" y="201">occaecat cupidatat non proident, sunt in culpa qui officia deserunt</text>
    <text x="383" y="220">mollit anim id est laborum.</text>
    <text x="383" y="255">Sed ut perspiciatis unde omnis iste natus error sit voluptatem accusan-</text>
    <text x="383" y="273">tium doloremque laudantium, totam rem aperiam, eaque ipsa quae ab</text>
    <text x="383" y="292">illo inventore veritatis et quasi architecto beatae vitae dicta sunt expli-</text>
    <text x="383" y="310">cabo. Nemo enim ipsam voluptatem quia voluptas sit aspernatur aut</text>
    <text x="383" y="329">odit aut fugit, sed quia consequuntur magni dolores eos qui ratione vo-</text>
    <text x="383" y="347">luptatem sequi nesciunt.</text>
  </g>
  <text x="27" y="411" class="body ink" font-size="8">© 2025, Torvane, LLC. All rights Reserved.</text>
  <line x1="215" y1="408" x2="707" y2="408" stroke="var(--red)" stroke-width="2"/>
  <circle cx="718" cy="408" r="11" fill="#fff" stroke="var(--red)" stroke-width="1.5"/>
  <text x="718" y="411" class="body ink" font-size="8" text-anchor="middle">03</text>
</svg>

<!-- Process timeline -->
<svg class="slide s-process" viewBox="0 0 758 427" xmlns="http://www.w3.org/2000/svg">
  <defs>
    <filter id="lift" x="-30%" y="-30%" width="160%" height="160%"><feDropShadow dx="0" dy="1" stdDeviation="2" flood-opacity="0.18"/></filter>
  </defs>
  <text x="27" y="43" class="head" font-size="30"><tspan class="red">Title</tspan><tspan class="ink"> Goes Here</tspan></text>
  <circle cx="589" cy="33" r="16" class="red"/>
  <text x="613" y="44" class="brand" font-size="30">Torvane</text>
  <g class="bold" font-size="12" text-anchor="middle">
    <text x="254" y="80" class="red">Header Text here</text>
    <text x="503" y="80" class="red">Header Text here</text>
  </g>
  <g class="body muted" font-size="8.5" text-anchor="middle">
    <text x="254" y="100">Lorem ipsum dolor sit amet,</text><text x="254" y="113">consectetur adipiscing elit, sed</text><text x="254" y="126">dolore magna aliqua.</text>
    <text x="503" y="100">Lorem ipsum dolor sit amet,</text><text x="503" y="113">consectetur adipiscing elit, sed</text><text x="503" y="126">dolore magna aliqua.</text>
  </g>
  <g fill="none" stroke-width="9">
    <circle cx="129" cy="226" r="62" stroke="var(--track)"/>
    <circle cx="254" cy="226" r="62" stroke="var(--track)"/>
    <circle cx="379" cy="226" r="62" stroke="var(--track)"/>
    <circle cx="504" cy="226" r="62" stroke="var(--track)"/>
    <circle cx="628" cy="226" r="62" stroke="var(--track)"/>
    <path d="M67 226 A62 62 0 0 1 191 226" stroke="#444"/>
    <path d="M192 226 A62 62 0 0 0 316 226" stroke="var(--red)"/>
    <path d="M317 226 A62 62 0 0 1 441 226" stroke="#444"/>
    <path d="M442 226 A62 62 0 0 0 566 226" stroke="var(--red)"/>
    <path d="M566 226 A62 62 0 0 1 690 226" stroke="#444"/>
  </g>
  <g fill="#fff" stroke-width="2">
    <circle cx="191" cy="226" r="8" stroke="var(--red)"/>
    <circle cx="316" cy="226" r="8" stroke="#444"/>
    <circle cx="441" cy="226" r="8" stroke="var(--red)"/>
    <circle cx="565" cy="226" r="8" stroke="#444"/>
    <circle cx="690" cy="226" r="8" stroke="var(--red)"/>
  </g>
  <g fill="#fff" filter="url(#lift)">
    <circle cx="129" cy="226" r="30"/><circle cx="254" cy="226" r="30"/><circle cx="379" cy="226" r="30"/>
    <circle cx="504" cy="226" r="30"/><circle cx="628" cy="226" r="30"/>
  </g>
  <g fill="none" stroke-width="1.3" stroke-linecap="round" stroke-linejoin="round">
    <g stroke="#444"><circle cx="121" cy="216" r="4"/><circle cx="137" cy="216" r="4"/><path d="M114 240v-10h30v10M120 230v-4h18v4"/></g>
    <g stroke="var(--red)"><rect x="244" y="208" width="14" height="10" rx="1"/><circle cx="248" cy="228" r="4"/><path d="M241 242a7 7 0 0 1 14 0"/><circle cx="262" cy="234" r="6"/><path d="M262 231v6"/></g>
    <g stroke="#444"><rect x="376" y="209" width="15" height="13"/><path d="M379 219v-3M383 219v-6M387 219v-8"/><circle cx="370" cy="226" r="4"/><path d="M363 241a7 7 0 0 1 14 0"/></g>
    <g stroke="var(--red)"><rect x="490" y="210" width="10" height="9"/><rect x="506" y="212" width="11" height="8"/><circle cx="504" cy="228" r="4"/><path d="M495 242a9 9 0 0 1 18 0"/></g>
    <g stroke="#444"><circle cx="628" cy="220" r="7"/><circle cx="628" cy="220" r="2.5"/><path d="M614 228l8 12h12l8-12"/></g>
  </g>
  <g class="bold" font-size="12" text-anchor="middle" fill="var(--ink)">
    <text x="129" y="322">Header Text here</text>
    <text x="379" y="322">Header Text here</text>
    <text x="628" y="322">Header Text here</text>
  </g>
  <g class="body muted" font-size="8.5" text-anchor="middle">
    <text x="129" y="342">Lorem ipsum dolor sit amet,</text><text x="129" y="355">consectetur adipiscing elit, sed</text><text x="129" y="368">dolore magna aliqua.</text>
    <text x="379" y="342">Lorem ipsum dolor sit amet,</text><text x="379" y="355">consectetur adipiscing elit, sed</text><text x="379" y="368">dolore magna aliqua.</text>
    <text x="628" y="342">Lorem ipsum dolor sit amet,</text><text x="628" y="355">consectetur adipiscing elit, sed</text><text x="628" y="368">dolore magna aliqua.</text>
  </g>
  <text x="27" y="411" class="body ink" font-size="8">© 2025, Torvane, LLC. All rights Reserved.</text>
  <line x1="215" y1="408" x2="707" y2="408" stroke="var(--red)" stroke-width="2"/>
  <circle cx="718" cy="408" r="11" fill="#fff" stroke="var(--red)" stroke-width="1.5"/>
  <text x="718" y="411" class="body ink" font-size="8" text-anchor="middle">07</text>
</svg>

<!-- Services -->
<svg class="slide s-services" viewBox="0 0 758 427" xmlns="http://www.w3.org/2000/svg">
  <defs>
    <filter id="card" x="-10%" y="-10%" width="120%" height="125%"><feDropShadow dx="0" dy="2" stdDeviation="3" flood-opacity="0.12"/></filter>
  </defs>
  <text x="27" y="43" class="head" font-size="30"><tspan class="red">Our</tspan><tspan class="ink"> Services</tspan></text>
  <circle cx="589" cy="33" r="16" class="red"/>
  <text x="613" y="44" class="brand" font-size="30">Torvane</text>
  <g fill="none" stroke="#555" stroke-width="1">
    <polyline points="282,144 315,144 315,166 345,166"/>
    <polyline points="476,144 446,144 446,166 416,166"/>
    <polyline points="282,311 315,311 315,288 345,288"/>
    <polyline points="476,311 446,311 446,288 416,288"/>
  </g>
  <circle cx="380" cy="226" r="68" fill="#fff" filter="url(#card)"/>
  <circle cx="341" cy="226" r="9" class="red"/>
  <text x="355" y="232" class="brand" font-size="18">Torvane</text>
  <g fill="#fff" filter="url(#card)">
    <rect x="43" y="84" width="219" height="119" rx="4"/>
    <rect x="495" y="84" width="219" height="119" rx="4"/>
    <rect x="43" y="250" width="219" height="119" rx="4"/>
    <rect x="495" y="250" width="219" height="119" rx="4"/>
  </g>
  <g class="red">
    <circle cx="263" cy="144" r="19"/><circle cx="495" cy="144" r="19"/>
    <circle cx="263" cy="311" r="19"/><circle cx="495" cy="311" r="19"/>
  </g>
  <g fill="none" stroke="#fff" stroke-width="1.3" stroke-linecap="round">
    <circle cx="263" cy="139" r="5"/><path d="M254 152q9-6 18 0"/>
    <rect x="489" y="136" width="12" height="10"/><path d="M487 152h16"/>
    <rect x="256" y="303" width="14" height="16"/><path d="M259 308h8M259 312h8"/>
    <path d="M488 318l14-14M488 304l14 14"/>
  </g>
  <g class="bold ink" font-size="12.5" text-anchor="middle">
    <text x="154" y="114">Lorem ipsum dolor amet,</text><text x="154" y="130">consectetur adipiscing</text>
    <text x="606" y="114">Lorem ipsum dolor amet,</text><text x="606" y="130">consectetur adipiscing</text>
    <text x="154" y="280">Lorem ipsum dolor amet,</text><text x="154" y="296">consectetur adipiscing</text>
    <text x="606" y="280">Lorem ipsum dolor amet,</text><text x="606" y="296">consectetur adipiscing</text>
  </g>
  <g class="body muted" font-size="9.5" text-anchor="middle">
    <text x="150" y="152">Ut enim minim veniam, quis nostrud</text><text x="150" y="166">exercitation ullamco laboris aliquip</text><text x="150" y="180">commodo consequat.</text>
    <text x="610" y="152">Ut enim minim veniam, quis nostrud</text><text x="610" y="166">exercitation ullamco laboris aliquip</text><text x="610" y="180">commodo consequat.</text>
    <text x="150" y="318">Ut enim minim veniam, quis nostrud</text><text x="150" y="332">exercitation ullamco laboris aliquip</text><text x="150" y="346">commodo consequat.</text>
    <text x="610" y="318">Ut enim minim veniam, quis nostrud</text><text x="610" y="332">exercitation ullamco laboris aliquip</text><text x="610" y="346">commodo consequat.</text>
  </g>
  <text x="27" y="411" class="body ink" font-size="8">© 2025, Torvane, LLC. All rights Reserved.</text>
  <line x1="215" y1="408" x2="707" y2="408" stroke="var(--red)" stroke-width="2"/>
  <circle cx="718" cy="408" r="11" fill="#fff" stroke="var(--red)" stroke-width="1.5"/>
  <text x="718" y="411" class="body ink" font-size="8" text-anchor="middle">04</text>
</svg>

<!-- Contact -->
<svg class="slide s-contact" viewBox="0 0 758 427" xmlns="http://www.w3.org/2000/svg">
  <defs>
    <linearGradient id="contactPhoto" x1="0" y1="0" x2="1" y2="1">
      <stop offset="0" stop-color="#c7353c"/>
      <stop offset="1" stop-color="#b3242b"/>
    </linearGradient>
  </defs>
  <g role="img" aria-label="Red-tinted photo of a team working in an office">
    <rect x="407" y="0" width="351" height="427" fill="url(#contactPhoto)"/>
  </g>
  <circle cx="67" cy="63" r="25" class="red"/>
  <text x="102" y="79" class="brand" font-size="44">Torvane</text>
  <text x="42" y="256" class="head" font-size="50" letter-spacing="-2"><tspan class="ink">Thank</tspan><tspan class="red"> You</tspan></text>
  <g fill="#444">
    <circle cx="406" cy="93" r="35"/><circle cx="406" cy="213" r="35"/><circle cx="406" cy="333" r="35"/>
  </g>
  <path d="M394 80c2-2 5-2 6 0l3 6c1 2 0 3-1 4l-2 2c2 5 6 9 11 11l2-2c1-1 3-2 4-1l6 3c2 1 2 4 0 6l-3 3c-3 3-10 1-18-7s-10-15-8-18z" fill="#fff"/>
  <g fill="none" stroke="#fff" stroke-width="2.5">
    <circle cx="406" cy="213" r="17"/><ellipse cx="406" cy="213" rx="7" ry="17"/>
    <path d="M389 213h34M392 204h28M392 222h28"/>
    <rect x="389" y="322" width="34" height="23" stroke-linejoin="round"/>
    <path d="M389 322l17 13 17-13M389 345l12-11M423 345l-12-11"/>
  </g>
  <g class="body white">
    <text x="462" y="85" font-size="11">Phone Number</text>
    <text x="462" y="111" font-size="16" font-weight="600">+1 (555) 014-2290</text>
    <text x="462" y="205" font-size="11">Website</text>
    <text x="462" y="231" font-size="16" font-weight="600">www.torvanelabs.com/</text>
    <text x="462" y="325" font-size="11">E-mail Address</text>
    <text x="462" y="351" font-size="16" font-weight="600">info@torvanelabs.com</text>
  </g>
</svg>

</div>
</body>
</html>
```